Healthcare and Professional IT Services Company need a redesigned business card

We are a IT Services company that targets small medical practices and professional business such as Attorneys, Accounts, Architects etc. We want to communicate a professional yet friendly image using recent logo redesign here on Sketchforge. Like to see the colors blue and orange in the design. Must use the Copper Lantern Technology as displayed in the new logo - then also want to incorporate the fish logo as well.

Target Market(s)

Small medical and professional services

Industry/Entity Type

It Company

Contact Information for Business Card

The usual stuff, place for name address phone website. Also maybe our tagline which is "lit up by technology"

Requirements
Must have
• My new logo and the fish somewhere on the card

```html
<!DOCTYPE html>
<html lang="en">
<head>
<meta charset="utf-8">
<title>Copper Lantern Technology – Business Card</title>
<link rel="stylesheet" href="https://fonts.googleapis.com/css2?family=Quicksand:wght@400;500;700&display=swap">
<style>
  :root {
    --page-bg: #e9e6e1;
    --card-bg: #ffffff;
    --brand-blue: #1b8cc7;
    --brand-blue-deep: #1577b0;
    --brand-sky: #3cb3e3;
    --brand-orange: #f0ad1f;
    --text-grey: #6b6f73;
    --text-dark: #4a4e52;
    --icon-grey: #9cb6c8;
  }
  * { box-sizing: border-box; margin: 0; padding: 0; }
  html, body {
    width: 1200px; height: 780px; overflow: hidden;
    background: var(--page-bg);
    font-family: "Quicksand", sans-serif;
  }
  .sheet {
    width: 1200px; height: 780px;
    display: flex; align-items: center; justify-content: center; gap: 40px;
  }
  .card {
    position: relative;
    width: 540px; height: 310px;
    background: var(--card-bg);
    box-shadow: 0 6px 18px rgba(0,0,0,.18);
    overflow: hidden;
  }
  .card-waves { position: absolute; inset: 0; width: 100%; height: 100%; }

  /* Front */
  .fish-mark {
    position: absolute;
    background: radial-gradient(circle at 45% 45%, #e3f3fb 0%, #bfe3f4 70%, #a6d6ee 100%);
    border-radius: 46% 54% 50% 50%;
  }
  .front .fish-mark { left: 40px; top: 40px; width: 110px; height: 90px; }
  .wordmark {
    color: var(--brand-sky);
    font-weight: 700;
    line-height: 1.05;
    letter-spacing: -0.5px;
  }
  .front .wordmark { position: absolute; left: 36px; top: 140px; font-size: 22px; width: 180px; }
  .tagline { color: var(--brand-blue); font-weight: 500; }
  .front .tagline { position: absolute; left: 38px; top: 196px; font-size: 13px; }

  .person { position: absolute; left: 232px; top: 34px; }
  .person-name { color: var(--brand-sky); font-weight: 700; font-size: 20px; }
  .person-role { color: var(--text-grey); font-size: 12px; margin-top: 1px; }

  .social-row { position: absolute; left: 232px; top: 88px; display: flex; gap: 8px; }
  .social-row span { width: 18px; height: 18px; border-radius: 3px; background: var(--icon-grey); }

  .contact-list { position: absolute; left: 232px; top: 114px; list-style: none; }
  .contact-list li {
    display: flex; align-items: center; gap: 8px;
    color: var(--text-dark); font-size: 12.5px; font-weight: 500; line-height: 19px;
  }
  .contact-list svg { width: 12px; height: 12px; flex: none; }

  .address {
    position: absolute; right: 26px; bottom: 24px;
    color: #fff; font-size: 13px; font-weight: 500; letter-spacing: .2px;
  }

  /* Back */
  .back .fish-mark { left: 200px; top: 40px; width: 120px; height: 96px; }
  .back .wordmark { position: absolute; left: 150px; top: 148px; font-size: 38px; width: 360px; color: var(--brand-blue); }
  .back .tagline { position: absolute; left: 154px; top: 244px; font-size: 15px; letter-spacing: 3px; }
</style>
</head>
<body>
<main class="sheet">

  <section class="card front" aria-label="Business card front">
    <svg class="card-waves" viewBox="0 0 540 310" preserveAspectRatio="none" aria-hidden="true">
      <path d="M0 272 C150 268 300 250 400 217 C470 194 510 182 540 178" fill="none" stroke="var(--brand-orange)" stroke-width="7"/>
      <path d="M0 310 L0 292 C160 288 310 272 410 238 C475 216 515 206 540 202 L540 310 Z" fill="var(--brand-blue)"/>
    </svg>

    <div class="fish-mark" role="img" aria-label="Cartoon fish mascot in light blue outline"></div>
    <div class="wordmark">Copper Lantern Technology</div>
    <div class="tagline">lit up by technology</div>

    <div class="person">
      <div class="person-name">Employee Name</div>
      <div class="person-role">Director</div>
    </div>

    <div class="social-row" aria-label="Social links">
      <span></span><span></span><span></span><span></span>
    </div>

    <ul class="contact-list">
      <li>
        <svg viewBox="0 0 12 12"><rect width="12" height="12" rx="2" fill="var(--brand-sky)"/><path d="M3.5 3 L5 3 L5.6 4.8 L4.8 5.4 C5.3 6.5 5.9 7.1 6.9 7.6 L7.5 6.8 L9.2 7.4 L9.2 8.9 C6 9 3 6.3 3.5 3 Z" fill="#fff"/></svg>
        0455 218 903
      </li>
      <li>
        <svg viewBox="0 0 12 12"><rect width="12" height="12" rx="2" fill="var(--brand-sky)"/><rect x="2.5" y="3.5" width="7" height="5" fill="none" stroke="#fff" stroke-width="1"/><path d="M2.5 3.5 L6 6.3 L9.5 3.5" fill="none" stroke="#fff" stroke-width="1"/></svg>
        hello@copperlantern.net
      </li>
      <li>
        <svg viewBox="0 0 12 12"><rect width="12" height="12" rx="2" fill="var(--brand-sky)"/><circle cx="6" cy="6" r="3.4" fill="none" stroke="#fff" stroke-width="1"/><path d="M2.6 6 H9.4 M6 2.6 V9.4" stroke="#fff" stroke-width=".8"/></svg>
        www.copperlanterntech.com
      </li>
    </ul>

    <div class="address">P.O. Box 214, Marlow Ridge, Fenwick, USA</div>
  </section>

  <section class="card back" aria-label="Business card back">
    <svg class="card-waves" viewBox="0 0 540 310" preserveAspectRatio="none" aria-hidden="true">
      <path d="M70 0 C84 110 108 215 168 310" fill="none" stroke="var(--brand-orange)" stroke-width="6"/>
      <path d="M0 0 L52 0 C66 112 92 218 152 310 L0 310 Z" fill="var(--brand-blue-deep)"/>
    </svg>

    <div class="fish-mark" role="img" aria-label="Cartoon fish mascot in light blue outline"></div>
    <div class="wordmark">Copper Lantern Technology</div>
    <div class="tagline">lit up by technology</div>
  </section>

</main>
</body>
</html>
```